Business Card Design needed for logo design project

Our business needs a business card design. I'm not sure what format files are generally delivered back, but clearly I will need the ability to edit to add colleagues contact details.

Our logo is attached.

Brivomar is a 3D design services company, providing app, serious/educational game, VR and AR websites/applications to corporate clients.

Target Market(s)

Corporate blue-chip clients needing 3D design services

Industry/Entity Type

Business

Font styles to use
Sans Serif

Requirements
Must have
• Templated such that I can add details (name, phone number etc). Needs to include logo from previous project winner - attached.

```html
<!DOCTYPE html>
<html lang="en">
<head>
<meta charset="utf-8">
<title>Brivomar Business Card</title>
<link rel="stylesheet" href="https://fonts.googleapis.com/css2?family=Arimo:wght@400;700&display=swap">
<style>
  :root {
    --canvas-bg: #2b2b2b;
    --card-black: #0d0d0d;
    --card-black-light: #1e1e1e;
    --brand-red: #e41e26;
    --text-white: #ffffff;
    --text-soft: #d6d6d6;
    --text-grey: #6a6a6a;
  }
  * { box-sizing: border-box; margin: 0; padding: 0; }
  html, body { width: 1200px; height: 900px; overflow: hidden; }
  body {
    background: var(--canvas-bg);
    font-family: "Arimo", Arial, sans-serif;
    position: relative;
  }
  .card {
    position: absolute;
    left: 330px;
    width: 540px;
    height: 310px;
    border-radius: 18px;
    background: linear-gradient(135deg, var(--card-black-light), var(--card-black) 60%);
    overflow: hidden;
  }
  .card--back { top: 110px; }
  .card--front { top: 480px; }

  /* Back */
  .services {
    position: absolute;
    left: 300px;
    top: 46px;
    list-style: none;
    color: var(--text-soft);
    font-size: 15px;
    line-height: 24px;
  }
  .services li::before {
    content: "";
    display: inline-block;
    width: 6px; height: 6px;
    border-radius: 50%;
    background: var(--brand-red);
    margin-right: 9px;
    vertical-align: middle;
  }
  .back-brand {
    position: absolute;
    left: 130px;
    bottom: 44px;
    display: flex;
    align-items: center;
    gap: 16px;
  }
  .back-brand__dot {
    width: 60px; height: 60px;
    border-radius: 50%;
    background: var(--brand-red);
  }
  .back-brand__name {
    font-size: 52px;
    font-weight: 400;
    letter-spacing: 3px;
    color: var(--text-grey);
  }

  /* Front */
  .front-circle {
    position: absolute;
    left: -120px;
    top: 30px;
    width: 330px; height: 330px;
    border-radius: 50%;
    background: var(--brand-red);
  }
  .contact {
    position: absolute;
    left: 262px;
    top: 34px;
  }
  .contact__name {
    color: var(--text-white);
    font-size: 26px;
    font-weight: 700;
  }
  .contact__title {
    color: var(--brand-red);
    font-size: 14px;
    margin-top: 2px;
  }
  .contact__list {
    list-style: none;
    margin-top: 12px;
    color: var(--text-soft);
    font-size: 14px;
  }
  .contact__list li {
    display: flex;
    align-items: center;
    gap: 8px;
    height: 22px;
  }
  .contact__list .contact__web {
    margin-top: 10px;
    font-weight: 700;
    color: var(--text-white);
    font-size: 15px;
  }
  .icon {
    width: 16px; height: 16px;
    border-radius: 50%;
    background: var(--brand-red);
    display: inline-flex;
    align-items: center;
    justify-content: center;
    flex: none;
  }
  .front-brand {
    position: absolute;
    right: 28px;
    bottom: 40px;
    color: var(--brand-red);
    font-size: 50px;
    font-weight: 400;
    letter-spacing: 3px;
  }
</style>
</head>
<body>
  <section class="card card--back">
    <ul class="services">
      <li>3D design services</li>
      <li>Application</li>
      <li>Serious/educational game</li>
      <li>VR and AR</li>
      <li>Websites/applications</li>
    </ul>
    <div class="back-brand">
      <span class="back-brand__dot"></span>
      <span class="back-brand__name">BRIVOMAR</span>
    </div>
  </section>

  <section class="card card--front">
    <div class="front-circle"></div>
    <div class="contact">
      <h1 class="contact__name">DEAN HALLOWAY</h1>
      <p class="contact__title">Your title here</p>
      <ul class="contact__list">
        <li>
          <span class="icon">
            <svg width="10" height="10" viewBox="0 0 10 10"><path d="M2 1 L4 1 L4.6 3 L3.5 3.8 Q4.5 5.8 6.2 6.5 L7 5.4 L9 6 L9 8 Q8.5 9 7.5 9 Q2.5 8 1 2.5 Q1 1.5 2 1 Z" fill="#0d0d0d"/></svg>
          </span>
          +61 XXX XXX XXX
        </li>
        <li>
          <span class="icon">
            <svg width="10" height="10" viewBox="0 0 10 10"><rect x="1" y="2.5" width="8" height="5.5" fill="none" stroke="#0d0d0d" stroke-width="1"/><path d="M1 2.5 L5 5.5 L9 2.5" fill="none" stroke="#0d0d0d" stroke-width="1"/></svg>
          </span>
          dean@brivomar.com.au
        </li>
        <li>
          <span class="icon"></span>
          @brivomar
        </li>
        <li class="contact__web">
          <span class="icon">
            <svg width="10" height="10" viewBox="0 0 10 10"><circle cx="5" cy="5" r="3.5" fill="none" stroke="#0d0d0d" stroke-width="1"/><path d="M1.5 5 H8.5 M5 1.5 V8.5" stroke="#0d0d0d" stroke-width="0.8"/></svg>
          </span>
          www.brivomar.com.au
        </li>
      </ul>
    </div>
    <div class="front-brand">BRIVOMAR</div>
  </section>
</body>
</html>
```